Very Simple/Minimal Business Card Design Project

The company operates in the industrial maritime infrastructure sector in Brazil. You can find more information on our website www.navelquor.com.br WE NEED TO LOOK POWERFUL AND SERIOUS
I have attached a copy of the old cards. We would like something more professional / industrial / sexy that also includes the position.

The card can be double sided or not. We would like you to propose as many options.

Thank you
Updates

Many thanks, do let me know if you have any questions. I am under a lot of time pressure to try and have them printed over the next days or so.

Please could you use the following information

for the address: Rua Tapiraçu, 418 - Centro, Rio de Janeiro, 20135-070, Brasil

for the mobile: +55 21 8372 9041
for the landline: +55 21 4067 3859

and position:  Diretor Geral

Thakn you

Target Market(s)

Shipowners, bankers, industrial companies

Industry/Entity Type

Industrial

Requirements
Must have
• POWERFUL
SERIOUS
SOLID
BIG CORPORATION

```html
<!DOCTYPE html>
<html lang="pt-BR">
<head>
<meta charset="utf-8">
<title>Navelquor – Cartão de Visita</title>
<link rel="stylesheet" href="https://fonts.googleapis.com/css2?family=Cabin:wght@400;600;700&display=swap">
<style>
  :root {
    --backdrop: #1a1a1a;
    --card: #ffffff;
    --navy: #0d2a6e;
    --soft-blue: #4a68b4;
    --brand-green: #17a03c;
  }
  * { margin: 0; padding: 0; box-sizing: border-box; }
  html, body {
    width: 1200px; height: 960px; overflow: hidden;
    background: var(--backdrop);
    font-family: "Cabin", sans-serif;
  }
  .business-card {
    position: absolute; left: 180px; top: 240px;
    width: 840px; height: 480px;
    background: var(--card);
    color: var(--navy);
  }
  .brand {
    position: absolute; left: 48px; top: 44px;
    display: flex; align-items: center; gap: 14px;
  }
  .brand-mark { width: 58px; height: 58px; background: var(--brand-green); border-radius: 6px; }
  .brand-name {
    font-weight: 700; font-size: 54px; letter-spacing: 2px;
    color: var(--navy); line-height: 1;
  }
  .holder-name {
    position: absolute; left: 48px; top: 160px;
    font-size: 66px; font-weight: 400; color: var(--soft-blue); line-height: 1;
  }
  .holder-role {
    position: absolute; left: 50px; top: 236px;
    font-size: 26px; font-weight: 600; letter-spacing: 1px;
    text-transform: uppercase; color: var(--navy); line-height: 1;
  }
  .holder-email {
    position: absolute; right: 48px; top: 234px;
    font-size: 26px; color: var(--navy); line-height: 1.1;
  }
  .contact {
    position: absolute; left: 48px; top: 334px;
    font-size: 24px; line-height: 34px; color: var(--navy);
  }
  .contact .web { color: var(--soft-blue); }
  .address {
    position: absolute; right: 48px; top: 368px;
    font-size: 22px; line-height: 30px; text-align: right;
    font-style: normal; color: var(--navy);
  }
</style>
</head>
<body>
  <main class="business-card">
    <div class="brand">
      <span class="brand-mark" aria-hidden="true"></span>
      <span class="brand-name">NAVELQUOR</span>
    </div>
    <h1 class="holder-name">Tomas Harcourt</h1>
    <p class="holder-role">Diretor Geral</p>
    <p class="holder-email">tomas@navelquor.com.br</p>
    <div class="contact">
      <p>Tf. + 55 21 4067 3859</p>
      <p>M: + 55 21 8372 9041</p>
      <p class="web">www.navelquor.com.br</p>
    </div>
    <address class="address">
      Rua Tapiraçu, 418<br>
      Centro<br>
      CEP 20135-070&nbsp; Rio de Janeiro
    </address>
  </main>
</body>
</html>
```